New Year Resolution Infographic

We are a weight loss company that provides holistic, natural nutrition programs to consumers -- you can see our Web site at www.TrimLark.com We need a simple infographic to be shared on social media and via email for New Year's day. The topic for the infographic is "how to set and keep your weight loss resolution". We've outlined 5 process steps for consumers to follow to assist with their weight loss resolutions, and we would like to depict this graphically.

Target Market(s)

Women age 35-65 who are planning to make a resolution to lose weight in the new year.

Industry/Entity Type

Health And Wellness

Font styles to use
Sans Serif

Colors
0392cd
9bcb3c

Requirements
Must have
• Initial graphic showing failure stats (see copy)
• Graphic showing process steps in making/keeping a resolution (see copy)
• TrimLark Logo

```html
<!DOCTYPE html>
<html lang="en">
<head>
<meta charset="utf-8">
<title>TrimLark – How to Set and Reach Your Weight Loss Resolution</title>
<link href="https://fonts.googleapis.com/css2?family=Montserrat:wght@600;700;800;900&family=Oswald:wght@400;500;600&display=swap" rel="stylesheet">
<style>
:root{
  --page:#ecebe8;
  --navy:#0a2740;
  --deep:#0c3658;
  --blue:#0392cd;
  --mid:#0f6ea6;
  --green:#9bcb3c;
  --white:#ffffff;
  --ink:#1d2a36;
  --tile:#3da6d8;
}
*{box-sizing:border-box;margin:0;padding:0}
html,body{width:1200px;height:2332px;overflow:hidden;background:var(--page)}
.sheet{position:absolute;left:283px;top:32px;width:634px;height:2268px;overflow:hidden;background:var(--navy);font-family:"Oswald",sans-serif;color:var(--white)}
.abs{position:absolute}

/* header */
.header{left:0;top:0;width:634px;height:200px;background:linear-gradient(#ffffff,#e6e9ec)}
.scale-photo{left:18px;top:0;width:118px;height:84px;border-radius:0 0 10px 10px;background:radial-gradient(circle at 50% 40%,#d9dcdf 0 30%,#4a4f55 32% 60%,#2a2e33 62%)}
.brand{left:170px;top:8px;display:flex;align-items:center;gap:12px;font-family:"Montserrat",sans-serif;font-weight:700;font-size:46px;color:var(--blue);letter-spacing:1px}
.brand-dot{width:34px;height:34px;border-radius:50%;background:var(--green)}
.tape{left:0;top:96px;width:634px;height:104px;background:linear-gradient(#f7f7f5,#dcdedf)}
.title{left:0;top:108px;width:634px;text-align:center;font-family:"Montserrat",sans-serif;font-weight:900;color:var(--ink);line-height:1.05}
.title .l1{font-size:37px}
.title .l2{font-size:31px}

/* intro */
.intro{left:0;top:200px;width:634px;height:232px;background:radial-gradient(ellipse at 50% 30%,#0f72aa,#0b3d66 80%)}
.tiles{left:34px;top:30px;display:flex;gap:6px}
.tile{width:46px;height:40px;background:var(--tile);border:2px solid #9fd4ee;color:var(--navy);font-family:"Montserrat",sans-serif;font-weight:700;font-size:22px;display:flex;align-items:center;justify-content:center}
.stat{top:96px;font-family:"Montserrat",sans-serif;font-weight:800;font-size:15px;line-height:1.15;text-transform:uppercase}
.stat .hi{color:var(--green)}
.stat-a{left:24px;width:270px}
.stat-b{left:326px;width:290px}
.stat-rule{left:310px;top:92px;width:2px;height:100px;background:rgba(255,255,255,.5)}

/* guide banner */
.guide{left:0;top:432px;width:634px;height:108px;background:var(--deep)}
.guide-lead{left:0;top:14px;width:634px;text-align:center;font-family:"Montserrat",sans-serif;font-weight:800;font-size:15px;color:var(--green)}
.guide-bar{left:0;top:44px;width:634px;height:56px;background:#081f34;display:flex;align-items:center;justify-content:center;font-family:"Montserrat",sans-serif;font-weight:800;font-size:25px;color:var(--green)}

/* steps */
.step{left:0;width:634px;border-top:2px dashed rgba(255,255,255,.55)}
.step-bright{background:linear-gradient(160deg,#1689c4,#0b4f84 70%)}
.step-dark{background:linear-gradient(160deg,#0d4670,#0a2a48 75%)}
.step-title{font-weight:500;font-size:42px;line-height:1;letter-spacing:1px}
.step-text{font-weight:400;font-size:14.5px;line-height:1.25;text-transform:uppercase;margin-top:14px}
.question{left:70px;top:40px;font-family:"Montserrat",sans-serif;font-weight:900;font-size:240px;line-height:1;color:var(--green)}
</style>
</head>
<body>
<div class="sheet">

  <header class="abs header">
    <div class="abs tape" role="img" aria-label="Tape measure band"></div>
    <div class="abs scale-photo" role="img" aria-label="Photo of a bathroom scale dial"></div>
    <div class="abs brand"><span>TrimLark</span><span class="brand-dot"></span></div>
    <h1 class="abs title"><div class="l1">HOW TO SET AND REACH</div><div class="l2">YOUR WEIGHT LOSS RESOLUTION</div></h1>
  </header>

  <section class="abs intro">
    <div class="abs tiles">
      <span class="tile">R</span><span class="tile">E</span><span class="tile">S</span><span class="tile">O</span><span class="tile">L</span><span class="tile">U</span><span class="tile">T</span><span class="tile">I</span><span class="tile">O</span><span class="tile">N</span><span class="tile">S</span>
    </div>
    <p class="abs stat stat-a"><span class="hi">Weight loss is the #1 New Year resolution, but</span><br>We know that resolutions are very difficult to keep.</p>
    <div class="abs stat-rule"></div>
    <p class="abs stat stat-b"><span class="hi">While 45% of Americans make New Year resolutions,</span><br>Only 8% succeed in keeping those resolutions.</p>
  </section>

  <section class="abs guide">
    <p class="abs guide-lead">HERE IS A QUICK GUIDE TO SETTING AND REACHING YOUR</p>
    <div class="abs guide-bar">WEIGHT LOSS RESOLUTION THIS YEAR</div>
  </section>

  <section class="abs step step-bright" style="top:540px;height:343px">
    <div class="abs question">?</div>
    <div class="abs" style="left:320px;top:62px;width:290px">
      <h2 class="step-title">1. REFLECT</h2>
      <p class="step-text">Get clear on why the achievement of your resolution is important. You'll need to come back to this if you falter!</p>
    </div>
  </section>

  <section class="abs step step-dark" style="top:883px;height:264px">
    <div class="abs" style="left:28px;top:70px;width:400px">
      <h2 class="step-title">2. RESOLVE</h2>
      <p class="step-text">Set a weight loss goal for the year that is realistic, then break this up into even shorter term goals of 30-60 days, with a specific diet and activity plan to guide you.</p>
    </div>
    <svg class="abs" style="left:455px;top:70px" width="150" height="130" viewBox="0 0 150 130" fill="none" stroke="#fff" stroke-width="4">
      <rect x="6" y="14" width="118" height="92" rx="8"/>
      <line x1="6" y1="34" x2="124" y2="34"/>
      <g stroke-linecap="round"><line x1="30" y1="6" x2="30" y2="22"/><line x1="55" y1="6" x2="55" y2="22"/><line x1="80" y1="6" x2="80" y2="22"/><line x1="105" y1="6" x2="105" y2="22"/></g>
      <g fill="#fff" stroke="none">
        <circle cx="26" cy="52" r="4"/><circle cx="46" cy="52" r="4"/><circle cx="66" cy="52" r="4"/><circle cx="86" cy="52" r="4"/><circle cx="106" cy="52" r="4"/>
        <circle cx="26" cy="72" r="4"/><circle cx="46" cy="72" r="4"/><circle cx="66" cy="72" r="4"/><circle cx="86" cy="72" r="4"/>
        <circle cx="26" cy="92" r="4"/><circle cx="46" cy="92" r="4"/>
      </g>
      <circle cx="118" cy="104" r="24" fill="#9bcb3c" stroke="none"/>
      <path d="M118 90v14l-7 8" stroke="#0a2740" stroke-width="3"/>
    </svg>
  </section>

  <section class="abs step step-bright" style="top:1147px;height:295px">
    <svg class="abs" style="left:60px;top:90px" width="120" height="120" viewBox="0 0 120 120">
      <rect x="30" y="26" width="60" height="40" fill="#9bcb3c" transform="rotate(-12 60 46)"/>
      <path d="M44 20l6-14 6 14zM62 20l8-16 6 16z" fill="#fff"/>
      <path d="M6 60l18 30h28l6 24M114 60l-18 30H68l-6 24" fill="none" stroke="#fff" stroke-width="7" stroke-linejoin="round" stroke-linecap="round"/>
    </svg>
    <div class="abs" style="left:250px;top:50px;width:360px">
      <h2 class="step-title">3. REPLACE</h2>
      <p class="step-text">Clear out your pantry and stock up with only healthy foods. Then work to build new activity and eating habits that take the place of your current habits.</p>
    </div>
  </section>

  <section class="abs step step-dark" style="top:1442px;height:249px">
    <div class="abs" style="left:28px;top:64px;width:410px">
      <h2 class="step-title">4. RECORD</h2>
      <p class="step-text">Track your progress daily, tell your family and friends about your resolution to create more accountability, and recruit a partner to share your journey.</p>
    </div>
    <svg class="abs" style="left:465px;top:60px" width="110" height="100" viewBox="0 0 110 100">
      <path d="M6 4v88h100" fill="none" stroke="#fff" stroke-width="4"/>
      <g fill="#9bcb3c"><rect x="16" y="62" width="16" height="26"/><rect x="38" y="52" width="16" height="36"/><rect x="60" y="58" width="16" height="30"/><rect x="82" y="40" width="16" height="48"/></g>
      <path d="M14 52l26-22 22 14 34-30" fill="none" stroke="#fff" stroke-width="4"/>
      <path d="M86 8h16v16" fill="none" stroke="#fff" stroke-width="4"/>
    </svg>
  </section>

  <section class="abs step step-bright" style="top:1691px;height:249px">
    <svg class="abs" style="left:72px;top:40px" width="130" height="170" viewBox="0 0 130 170">
      <path d="M30 100l-20 64 28-14 18 18 14-58zM100 100l20 64-28-14-18 18-14-58z" fill="none" stroke="#fff" stroke-width="4" stroke-linejoin="round"/>
      <circle cx="65" cy="62" r="58" fill="#0a4f84" stroke="#fff" stroke-width="4"/>
      <circle cx="65" cy="62" r="40" fill="#9bcb3c"/>
      <path d="M50 44h30v12a15 15 0 0 1-30 0zM62 70h6v10h-6zM54 82h22v5H54z" fill="#fff"/>
    </svg>
    <div class="abs" style="left:265px;top:40px;width:350px">
      <h2 class="step-title">5. REWARD</h2>
      <p class="step-text">Rather than using unhealthy food as a reward or cheat, give yourself healthy or relaxing experiences – such a spa treatment or taking a new fitness class.</p>
    </div>
  </section>

  <section class="abs" style="left:0;top:1924px;width:634px;height:218px;border-top:2px dashed rgba(255,255,255,.55)">
    <div class="abs" role="img" aria-label="Black and white photo of a tape measure around a waist" style="left:0;top:0;width:634px;height:218px;background:linear-gradient(175deg,#f4f4f4,#bfc3c6 60%,#8d9296)"></div>
    <p class="abs" style="left:40px;top:40px;width:560px;transform:rotate(-3deg);font-weight:600;font-size:30px;line-height:1.05;text-transform:uppercase;color:var(--green)"><span style="color:#3a3f44">TrimLark</span> can help you achieve your weight loss resolution in the new year.</p>
  </section>

  <footer class="abs" style="left:0;top:2142px;width:634px;height:126px;background:var(--deep)">
    <p class="abs" style="left:0;top:14px;width:634px;text-align:center;font-family:'Montserrat',sans-serif;font-weight:700;font-size:15px;color:var(--green)">WE INVITE YOU TO LEARN MORE AND CONTACT US FOR A FREE CONSULTATION.</p>
    <p class="abs" style="left:0;top:44px;width:634px;text-align:center;font-weight:600;font-size:50px;letter-spacing:7px;color:var(--green);text-transform:uppercase">www.TrimLark.com</p>
  </footer>

</div>
</body>
</html>
```